Email Banner (QuillStacks)

We require an email banner for our email promotions sent to prospect clients. The banner needs to contain the wording QuillStacks and use the same colour scheme as the logos attached.

This is for B2B professional's so needs to look like a place you would come to read technology articles.

```html
<!DOCTYPE html>
<html lang="en">
<head>
<meta charset="utf-8">
<title>QuillStacks Email Banner</title>
<link rel="stylesheet" href="https://fonts.googleapis.com/css2?family=Roboto:wght@400;500;700&family=Montserrat:wght@500;800&display=swap">
<style>
  :root {
    --page: #ffffff;
    --stage: #e4e7ea;
    --header: #f4f5f5;
    --navy: #1d2b4f;
    --ink-dark: #050b24;
    --red: #d12a2f;
    --text: #5b5e4f;
    --heading: #5d6152;
    --white: #ffffff;
    --label: #111827;
  }
  * { box-sizing: border-box; margin: 0; padding: 0; }
  html, body { width: 1200px; height: 729px; overflow: hidden; background: var(--page); }
  body { position: relative; font-family: "Roboto", Arial, sans-serif; }

  .brand { display: flex; align-items: center; gap: 5px; font-family: "Roboto", Arial, sans-serif; font-weight: 500; color: var(--navy); font-size: 13px; letter-spacing: .1px; }
  .brand-mark { width: 8px; height: 8px; background: var(--red); }
  .brand--light { color: var(--white); font-size: 14px; }

  .masthead { height: 31px; background: var(--header); display: flex; align-items: center; padding-left: 12px; }

  .hero { position: relative; height: 149px; overflow: hidden; }
  .hero-art { position: absolute; inset: 0; }
  .hero-title { position: absolute; left: 14px; bottom: 21px; color: var(--white); font-weight: 700; font-size: 13px; }
  .hero-title::after { content: ""; position: absolute; left: 1px; bottom: -6px; width: 29px; height: 2px; background: var(--white); }

  .art-network { background: radial-gradient(ellipse at 55% 10%, #8a2260 0%, transparent 45%), radial-gradient(ellipse at 90% 90%, #243a8c 0%, transparent 55%), linear-gradient(135deg, #070c2c 0%, #1b1848 45%, #35276f 100%); }
  .art-growth { background: radial-gradient(ellipse at 62% 45%, #4e2a8a 0%, #1a1245 30%, transparent 60%), #020207; }
  .art-chart { background: radial-gradient(ellipse at 45% 60%, #2f9d9c 0%, transparent 40%), radial-gradient(ellipse at 80% 15%, #6b2a63 0%, transparent 45%), linear-gradient(120deg, #0c2340 0%, #16475c 45%, #243b7a 100%); }
  .art-papers { background: radial-gradient(ellipse at 80% 20%, #c0306a 0%, transparent 50%), linear-gradient(120deg, #1c2b7a 0%, #4b2a8c 50%, #9b2a7a 80%, #2a3fb0 100%); }
  .art-peak { background: radial-gradient(ellipse at 52% 55%, #5b2a9a 0%, #1a1560 30%, transparent 60%), linear-gradient(100deg, #040410 0%, #0a0a30 60%, #0c1050 100%); }
  .art-speech { background: radial-gradient(ellipse at 75% 45%, #efe2cf 0%, #e9d6c4 16%, transparent 30%), linear-gradient(120deg, #e01848 0%, #e02a70 50%, #b54aa8 100%); }

  .email-stage { position: absolute; left: 42px; top: 42px; width: 403px; height: 645px; background: var(--stage); }
  .email { position: absolute; left: 44px; top: 39px; width: 318px; background: var(--white); }
  .email-body { height: 354px; padding: 40px 26px 0 38px; color: var(--text); }
  .greeting { font-size: 14px; font-weight: 500; color: var(--heading); margin-bottom: 14px; }
  .email-body p { font-size: 6.9px; line-height: 12px; margin-bottom: 7px; }
  .cta { display: block; margin: 35px 0 0 11px; width: 156px; height: 31px; border-radius: 16px; background: var(--red); color: var(--white); font-size: 10.5px; text-align: center; line-height: 31px; text-decoration: none; }
  .email-footer { height: 35px; background: var(--ink-dark); display: flex; align-items: center; justify-content: space-between; padding: 0 15px 0 16px; }
  .social { display: flex; gap: 6px; }
  .social span { width: 11px; height: 11px; border-radius: 50%; background: #e6e8ee; }

  .option { position: absolute; width: 317px; }
  .option-label { margin-top: 8px; font-family: "Montserrat", Arial, sans-serif; font-weight: 500; font-size: 11px; letter-spacing: .3px; color: var(--label); }
  .option-label b { font-weight: 800; }
</style>
</head>
<body>
  <section class="email-stage">
    <article class="email">
      <header class="masthead"><div class="brand"><span class="brand-mark"></span>QuillStacks</div></header>
      <div class="hero">
        <div class="hero-art art-network" role="img" aria-label="Abstract dark network of connected points in purple and blue"></div>
        <h1 class="hero-title">We Need Your Help</h1>
      </div>
      <div class="email-body">
        <h2 class="greeting">Hello My friend,</h2>
        <p>Lorem ipsum dolor sit amet, consectetur adipiscing elit. Fusce at neque a justo fringilla lobortis a ac felis. Cras ultrices lorem dolor, porta placerat ipsum sollicitudin ut. Suspendisse hendrerit eros sed mi condimentum feugiat. Morbi ornare libero in sem convallis laoreet.</p>
        <p>Praesent sit amet elit felis. Nam dignissim sem ex, eu blandit nunc tincidunt nec. Praesent enim sapien, scelerisque id mi cursus, ornare efficitur justo. Donec non semper enim. Nunc eget porta justo. Maecenas commodo, metus at rhoncus interdum, arcu justo dapibus nisi, nec euismod mi quam a elit.</p>
        <p>Sed posuere nisi dui, ut ultrices massa vehicula sed. In maximus, metus ut luctus ullamcorper, quam sem semper nibh, sit amet finibus felis libero sed velit. Nunc rutrum iaculis dictum.</p>
        <p>Suspendisse maximus eget est sit amet egestas. Pellentesque porta condimentum nisl, non gravida ante ullamcorper ut.</p>
        <a class="cta" href="#">Accept invition</a>
      </div>
      <footer class="email-footer">
        <div class="brand brand--light"><span class="brand-mark"></span>QuillStacks</div>
        <div class="social"><span></span><span></span><span></span><span></span></div>
      </footer>
    </article>
  </section>

  <section class="option" style="left:481px; top:42px;">
    <header class="masthead"><div class="brand"><span class="brand-mark"></span>QuillStacks</div></header>
    <div class="hero"><div class="hero-art art-network" role="img" aria-label="Abstract dark network of connected points in purple and blue"></div><h2 class="hero-title">We Need Your Help</h2></div>
    <p class="option-label">OPTION <b>01</b></p>
  </section>

  <section class="option" style="left:829px; top:42px;">
    <header class="masthead"><div class="brand"><span class="brand-mark"></span>QuillStacks</div></header>
    <div class="hero"><div class="hero-art art-growth" role="img" aria-label="Glowing purple growth chart rising above an open hand on black"></div><h2 class="hero-title">We Need Your Help</h2></div>
    <p class="option-label">OPTION <b>02</b></p>
  </section>

  <section class="option" style="left:481px; top:264px;">
    <header class="masthead"><div class="brand"><span class="brand-mark"></span>QuillStacks</div></header>
    <div class="hero"><div class="hero-art art-chart" role="img" aria-label="Hand touching a tablet with a glowing teal line chart"></div><h2 class="hero-title">We Need Your Help</h2></div>
    <p class="option-label">OPTION <b>03</b></p>
  </section>

  <section class="option" style="left:829px; top:265px;">
    <header class="masthead"><div class="brand"><span class="brand-mark"></span>QuillStacks</div></header>
    <div class="hero"><div class="hero-art art-papers" role="img" aria-label="Scattered contract and agreement papers tinted blue and magenta"></div><h2 class="hero-title">We Need Your Help</h2></div>
    <p class="option-label">OPTION <b>04</b></p>
  </section>

  <section class="option" style="left:481px; top:486px;">
    <header class="masthead"><div class="brand"><span class="brand-mark"></span>QuillStacks</div></header>
    <div class="hero"><div class="hero-art art-peak" role="img" aria-label="Glowing purple and blue light peak on a dark background"></div><h2 class="hero-title">We Need Your Help</h2></div>
    <p class="option-label">OPTION <b>05</b></p>
  </section>

  <section class="option" style="left:829px; top:486px;">
    <header class="masthead"><div class="brand"><span class="brand-mark"></span>QuillStacks</div></header>
    <div class="hero"><div class="hero-art art-speech" role="img" aria-label="Two paper speech bubbles on a pink to purple background"></div><h2 class="hero-title">We Need Your Help</h2></div>
    <p class="option-label">OPTION <b>06</b></p>
  </section>
</body>
</html>
```